Compnay PowerPoint Tempalte Design

I am needing a good base design and slide designs for interior and exterior company presentations. The template will need to be on the company brand with proper coloring and fonts. Able to be creative with layout options with a good example attached.
website for reference: www.crewvantor.com/

Target Market(s)

Professionals

Font styles to use
Other font styles liked:
• Helvetica

Requirements
Must have
• On Brand Colors, Clean, simple design

```html
<!DOCTYPE html>
<html lang="en">
<head>
<meta charset="utf-8">
<title>Crewvantor Presentation Template</title>
<link href="https://fonts.googleapis.com/css2?family=Inter:ital,wght@0,400;0,500;0,600;0,700;1,400&display=swap" rel="stylesheet">
<style>
:root{
  --page:#ececec;
  --green:#1d4a44;
  --teal:#2b6a62;
  --blue:#1b6b95;
  --navy-text:#1a5f8a;
  --dark:#2a2522;
  --white:#ffffff;
  --body:#222222;
  --muted:#555555;
}
*{margin:0;padding:0;box-sizing:border-box}
html,body{width:1200px;height:4310px;overflow:hidden}
body{background:var(--page);font-family:"Inter",Helvetica,Arial,sans-serif;position:relative;color:var(--body)}
.slide{position:absolute;left:43px;width:1107px;height:623px;background:var(--white);overflow:hidden}
.slide svg.fill{position:absolute;display:block}

/* header band */
.slide-header{position:absolute;left:0;top:0;width:100%;height:50px;background:var(--green)}
.slide-header h2{position:absolute;left:16px;top:0;line-height:50px;color:var(--white);font-size:27px;font-weight:600;letter-spacing:-.3px}
.page-tab{position:absolute;right:0;top:0;width:150px;height:50px}
.page-tab span{position:absolute;right:42px;top:0;line-height:50px;color:var(--white);font-size:20px;font-weight:500}

/* footer */
.slide-footer{position:absolute;left:0;bottom:12px;width:100%;height:17px;background:var(--green)}
.slide-footer small{position:absolute;right:24px;top:0;line-height:17px;color:var(--white);font-size:11px}
.footer-brand{position:absolute;left:0;bottom:4px;width:102px;height:32px;background:var(--white);font-size:15px;font-weight:700;color:var(--green);line-height:32px;text-align:center}

/* cover */
.cover{top:50px;background:var(--dark)}
.cover-frame{position:absolute;left:8px;top:13px;right:8px;bottom:13px;border:2px solid rgba(255,255,255,.85)}
.brand-mark{position:absolute;left:0;width:100%;text-align:center;color:var(--white);font-weight:700}
.cover .brand-mark{top:240px;font-size:66px;letter-spacing:-1px}
.cover-title{position:absolute;top:366px;width:100%;text-align:center;color:var(--white);font-size:44px;font-weight:700;letter-spacing:-1px}
.cover-sub{position:absolute;top:425px;left:150px;right:150px;text-align:center;color:var(--white);font-size:19px;line-height:35px;letter-spacing:-.3px}
.scroll-cue{position:absolute;left:535px;top:528px;width:37px;height:37px}

/* about */
.about{top:765px}
.about-text{position:absolute;left:26px;top:140px;width:469px;font-size:19.5px;line-height:32.4px;text-align:justify;letter-spacing:-.3px}

/* team */
.team{top:1481px}
.member{position:absolute;top:102px;width:320px;text-align:center}
.member .portrait{width:188px;height:188px;margin:0 auto}
.member h3{margin-top:20px;color:var(--navy-text);font-size:20px;font-weight:600;letter-spacing:-.3px}
.member .role{margin-top:4px;font-size:14px;color:var(--body)}
.member p{margin:12px auto 0;width:290px;font-size:15.5px;line-height:28px;color:var(--muted);letter-spacing:-.2px}
.social{display:flex;justify-content:center;gap:14px;margin-top:10px}
.social span{width:45px;height:45px;border-radius:50%;background:var(--green)}

/* quote */
.quote{top:2198px;background:var(--teal)}
.quote-mark{position:absolute;top:150px;width:100%;text-align:center;color:var(--white);font-size:170px;font-weight:700;line-height:1;height:110px;overflow:hidden}
.quote p{position:absolute;left:113px;top:282px;width:882px;color:var(--white);font-size:24px;font-style:italic;line-height:40px;text-align:justify;text-align-last:center;letter-spacing:-.3px}

/* services */
.services{top:2913px}
.service{position:absolute;top:100px;width:318px;height:415px}
.service span{position:absolute;left:0;bottom:22px;width:100%;text-align:center;color:var(--white);font-size:26px;font-weight:600;letter-spacing:-.4px}

/* closing */
.closing{top:3628px}
.closing .brand-mark{top:190px;font-size:72px;letter-spacing:-1px;font-weight:700}
.closing-title{position:absolute;top:292px;width:100%;text-align:center;color:var(--white);font-size:44px;font-weight:600;letter-spacing:-.5px}
.contact{position:absolute;top:378px;width:330px;text-align:center;font-size:16px;line-height:24px;color:var(--body)}
.contact .icon{width:62px;height:62px;margin:0 auto 27px;background:var(--white);box-shadow:0 2px 6px rgba(0,0,0,.18);display:flex;align-items:center;justify-content:center}
</style>
</head>
<body>

<!-- Cover -->
<section class="slide cover">
  <svg class="fill" width="1107" height="623" role="img" aria-label="Dim photograph of a city skyline at night">
    <defs><linearGradient id="sky" x1="0" y1="0" x2="0" y2="1"><stop offset="0" stop-color="#3a3430"/><stop offset="1" stop-color="#211c19"/></linearGradient></defs>
    <rect width="1107" height="623" fill="url(#sky)"/>
  </svg>
  <div class="cover-frame"></div>
  <div class="brand-mark">Crewvantor</div>
  <h1 class="cover-title">THIS IS YOUR PRESENTATION TITLE</h1>
  <p class="cover-sub">here we maintain a passion for excellence, striving to be better each and every day, so that our guests leave happy and our team members feel fulfilled.</p>
  <svg class="scroll-cue" viewBox="0 0 37 37"><circle cx="18.5" cy="18.5" r="17" fill="none" stroke="#fff" stroke-width="2"/><path d="M18.5 9v18M11.5 20l7 7 7-7" fill="none" stroke="#fff" stroke-width="2"/></svg>
</section>

<!-- About -->
<section class="slide about">
  <svg class="fill" width="1107" height="623" style="left:0;top:0">
    <polygon points="584,50 1107,50 1107,623 489,623" fill="#6a5444" role="img" aria-label="Photo of four smiling women sharing coffee at a café table"/>
    <polygon points="577,50 584,50 489,623 482,623" fill="var(--blue)"/>
  </svg>
  <header class="slide-header"><h2>ABOUT Crewvantor</h2>
    <svg class="page-tab" viewBox="0 0 150 50"><polygon points="18,0 150,0 150,50 0,50" fill="var(--blue)"/><polygon points="12,0 16,0 -2,50 -6,50" fill="#fff"/></svg>
    <span class="page-tab" style="width:auto;right:42px;line-height:50px;color:#fff;font-size:20px;font-weight:500;height:50px">Page 2</span>
  </header>
  <p class="about-text">Crewvantor is dedicated to cultivating a positive culture of leadership for its team members’ professional and personal development, and this person-focused mentality transfers throughout the company from partners to our teams to guests. We strive to ensure each team member feels valued in all aspects of their role, reinforcing the importance of fostering a self-sustaining culture of success where everyone makes a team effort to communicate and overcome adversity.</p>
  <div class="slide-footer" style="width:490px"></div>
  <div class="footer-brand">Crewvantor</div>
  <small style="position:absolute;right:24px;bottom:12px;line-height:17px;color:#fff;font-size:11px">Copyright 2021 Crewvantor. All rights reserved</small>
</section>

<!-- Team -->
<section class="slide team">
  <header class="slide-header"><h2 style="left:34px">Our Team</h2>
    <svg class="page-tab" viewBox="0 0 150 50"><polygon points="18,0 150,0 150,50 0,50" fill="var(--blue)"/></svg>
    <span class="page-tab" style="width:auto;right:42px;line-height:50px;color:#fff;font-size:20px;font-weight:500;height:50px">Page 3</span>
  </header>
  <div class="member" style="left:16px">
    <svg class="portrait" viewBox="0 0 188 188" role="img" aria-label="Portrait of Owen Marsh"><circle cx="94" cy="94" r="92" fill="#5a6e7c" stroke="var(--blue)" stroke-width="3"/></svg>
    <h3>OWEN MARSH</h3><div class="role">CEO</div>
    <p>Growing up in Wichita, Kansas, where Benny’s started, Owen has long felt a connection with the group that started the concept, enjoying the food,</p>
    <div class="social"><span></span><span></span><span></span><span></span></div>
  </div>
  <div class="member" style="left:378px">
    <svg class="portrait" viewBox="0 0 188 188" role="img" aria-label="Portrait of Lena Hartwell"><circle cx="94" cy="94" r="92" fill="#8a6552" stroke="var(--blue)" stroke-width="3"/></svg>
    <h3>LENA HARTWELL</h3><div class="role">CONTROLLER</div>
    <p>Lena Hartwell is a brilliant veteran of the finance and accounting industries, utilizing her experience to elevate Crewvantor and its team members</p>
    <div class="social"><span></span><span></span><span></span><span></span></div>
  </div>
  <div class="member" style="left:738px">
    <svg class="portrait" viewBox="0 0 188 188" role="img" aria-label="Portrait of Rafael Ortiz"><circle cx="94" cy="94" r="92" fill="#3d63b0" stroke="var(--blue)" stroke-width="3"/></svg>
    <h3>RAFAEL ORTIZ</h3><div class="role">COO</div>
    <p>Seizing opportunities to change peoples’ lives, in front of and behind the counter, Rafael Ortiz genuinely enjoys the people-aspect of the food</p>
    <div class="social"><span></span><span></span><span></span><span></span></div>
  </div>
  <div class="slide-footer"><small>Copyright 2021 Crewvantor. All rights reserved</small></div>
  <div class="footer-brand">Crewvantor</div>
</section>

<!-- Quote -->
<section class="slide quote">
  <svg class="fill" width="1107" height="623" role="img" aria-label="Teal-tinted photo of a cheering team"><rect width="1107" height="623" fill="#2c6059"/><rect width="1107" height="623" fill="#24524c" opacity=".4"/></svg>
  <div class="quote-mark">“</div>
  <p>Northpeak Ventures LLC is such a great place to work, especially because the communication between all levels of employees is outstanding. Plus, there is a willingness to work with one another, which adds to the really wonderful atmosphere among the staff.</p>
</section>

<!-- Services -->
<section class="slide services">
  <header class="slide-header"><h2 style="left:34px">WHAT WE DO</h2>
    <svg class="page-tab" viewBox="0 0 150 50"><polygon points="18,0 150,0 150,50 0,50" fill="var(--blue)"/></svg>
    <span class="page-tab" style="width:auto;right:42px;line-height:50px;color:#fff;font-size:20px;font-weight:500;height:50px">Page 5</span>
  </header>
  <div class="service" style="left:31px">
    <svg class="fill" width="318" height="415" role="img" aria-label="Photo of a restaurant kitchen counter with shelves"><defs><linearGradient id="g1" x1="0" y1="0" x2="0" y2="1"><stop offset="0" stop-color="#7a6a5a"/><stop offset=".55" stop-color="#a0552a"/><stop offset="1" stop-color="#2e2a28"/></linearGradient></defs><rect width="318" height="415" fill="url(#g1)"/></svg>
    <span>Restaurants</span>
  </div>
  <div class="service" style="left:389px">
    <svg class="fill" width="318" height="415" role="img" aria-label="Photo of a hand holding a house key"><defs><linearGradient id="g2" x1="0" y1="0" x2="0" y2="1"><stop offset="0" stop-color="#9c8a78"/><stop offset="1" stop-color="#6b4a34"/></linearGradient></defs><rect width="318" height="415" fill="url(#g2)"/></svg>
    <span>Real Estate</span>
  </div>
  <div class="service" style="left:747px">
    <svg class="fill" width="318" height="415" role="img" aria-label="Photo of hands signing a document"><defs><linearGradient id="g3" x1="0" y1="0" x2="0" y2="1"><stop offset="0" stop-color="#e6e4e2"/><stop offset="1" stop-color="#8a8480"/></linearGradient></defs><rect width="318" height="415" fill="url(#g3)"/></svg>
    <span>Development</span>
  </div>
  <div class="slide-footer"><small>Copyright 2021 Crewvantor. All rights reserved</small></div>
  <div class="footer-brand">Crewvantor</div>
</section>

<!-- Closing -->
<section class="slide closing">
  <svg class="fill" width="1107" height="410" role="img" aria-label="Dark photo of a smiling group of colleagues"><rect width="1107" height="410" fill="#2e2b29"/></svg>
  <div style="position:absolute;left:0;top:408px;width:100%;height:4px;background:var(--blue)"></div>
  <div class="brand-mark">Crewvantor</div>
  <div class="closing-title">THANK YOU</div>
  <div class="contact" style="left:60px">
    <div class="icon"><svg width="24" height="30" viewBox="0 0 24 30"><path d="M12 1C6 1 2 5.5 2 11c0 7 10 18 10 18s10-11 10-18C22 5.5 18 1 12 1z" fill="var(--blue)"/><circle cx="12" cy="11" r="4" fill="#fff"/></svg></div>
    1420 W. RIDGELINE AVE<br>SUITE 310 DENVER, CO 80204
  </div>
  <div class="contact" style="left:395px">
    <div class="icon"><svg width="28" height="28" viewBox="0 0 24 24"><path d="M6.6 10.8a15 15 0 0 0 6.6 6.6l2.2-2.2c.3-.3.7-.4 1-.2 1.1.4 2.3.6 3.6.6.6 0 1 .4 1 1V20c0 .6-.4 1-1 1A17 17 0 0 1 3 4c0-.6.4-1 1-1h3.5c.6 0 1 .4 1 1 0 1.3.2 2.5.6 3.6.1.3 0 .7-.2 1z" fill="var(--blue)"/></svg></div>
    Phone:<br>(555) 014-2290
  </div>
  <div class="contact" style="left:724px">
    <div class="icon"><svg width="30" height="22" viewBox="0 0 30 22"><rect x="1" y="1" width="28" height="20" fill="var(--blue)"/><path d="M1 1l14 11L29 1" fill="none" stroke="#fff" stroke-width="2"/></svg></div>
    Email:<br>info@crewvantor.com
  </div>
</section>

</body>
</html>
```